Hello,
Corinne Haskett Equestrian needs a business card. We are a high performance show jumping stables based at Willowmere Reserve in morningotn. We pride ourselves on producing high quality show jumping horses and competing our stock at a high level. My business card need to have my logo on it, and i would like it to have a classic design with a modern touch. I would like it to have quite a natural feel about it. It needs to be in a font which is easy to read as I spend a lot of time competing internationally and overseas, and i need to be able to give it out to breeders and contacts where English isnt their first language. I will need it to include the following details:
-Corinne Haskett Equestrian
-Based at Willowmere Reserve Ferncliff Heights
-Address: 17 Tremont Lane Ferncliff Heights Northvale 4870
-Mobile number: 0412605948
- website: www.corinnehaskettequestrian.example
Target Market(s)
For business adults who english may not be their first language
Industry/Entity Type
Business

```html
<!DOCTYPE html>
<html lang="en">
<head>
<meta charset="utf-8">
<title>Corinne Haskett Equestrian – Business Card</title>
<link rel="stylesheet" href="https://fonts.googleapis.com/css2?family=Cinzel:wght@400&family=Cormorant+Garamond:wght@500&display=swap">
<style>
  :root {
    --canvas-bg: #e9e6e1;
    --card-navy: #1f3b72;
    --card-navy-deep: #1a3366;
    --card-ink: #ffffff;
    --card-ink-soft: #dfe6f3;
    --card-shadow: rgba(20, 24, 40, 0.22);
  }
  * { margin: 0; padding: 0; box-sizing: border-box; }
  html, body {
    width: 1200px;
    height: 674px;
    overflow: hidden;
    background: var(--canvas-bg);
  }
  .stage {
    width: 1200px;
    height: 674px;
    display: flex;
    align-items: center;
    justify-content: center;
    gap: 60px;
  }
  .card {
    width: 525px;
    height: 300px;
    background: linear-gradient(160deg, var(--card-navy) 0%, var(--card-navy-deep) 100%);
    box-shadow: 0 14px 30px var(--card-shadow);
    color: var(--card-ink);
    position: relative;
    overflow: hidden;
  }
  .card-front {
    display: flex;
    align-items: center;
    justify-content: center;
  }
  .brand-name {
    font-family: "Cinzel", serif;
    font-weight: 400;
    font-size: 27px;
    letter-spacing: 1px;
    color: var(--card-ink);
    text-align: center;
    line-height: 1.25;
  }
  .card-back {
    padding: 44px 30px 0 30px;
    text-align: center;
  }
  .owner-name {
    font-family: "Cinzel", serif;
    font-weight: 400;
    font-size: 26px;
    letter-spacing: 1px;
    color: var(--card-ink);
    white-space: nowrap;
  }
  .base-line {
    font-family: "Cormorant Garamond", serif;
    font-weight: 500;
    font-size: 15px;
    color: var(--card-ink-soft);
    margin-top: 4px;
  }
  .contact-list {
    list-style: none;
    margin-top: 22px;
    font-family: "Cormorant Garamond", serif;
    font-weight: 500;
    font-size: 20px;
    line-height: 1.6;
    color: var(--card-ink);
  }
  .contact-web { font-size: 19px; margin-top: 6px; }
</style>
</head>
<body>
  <main class="stage">
    <section class="card card-front" aria-label="Card front">
      <p class="brand-name">Corinne Haskett<br>Equestrian</p>
    </section>

    <section class="card card-back" aria-label="Card back">
      <h1 class="owner-name">Corinne Haskett Equestrian</h1>
      <p class="base-line">Based at Willowmere Reserve, Ferncliff Heights</p>
      <ul class="contact-list">
        <li class="contact-address">17 Tremont Lane Ferncliff Heights Northvale 4870</li>
        <li class="contact-phone">041 260 5948</li>
        <li class="contact-web">www.corinnehaskettequestrian.example</li>
      </ul>
    </section>
  </main>
</body>
</html>
```